Brindale transport business cards

Front of card, Looking for my logo on one side of the card

Back of card,
Brindale Transport Maintenance
Onsite Cars, Trucks & trailer maintenance and repairs
Ronan Brindale
0452819036
Brindaletm@fernmail.com

```html
<!DOCTYPE html>
<html lang="en">
<head>
<meta charset="utf-8">
<title>Brindale transport business cards</title>
<link rel="stylesheet" href="https://fonts.googleapis.com/css2?family=Lato:wght@400;700;900&family=Russo+One&display=swap">
<style>
  :root {
    --backdrop: #3b3b3b;
    --card-white: #ffffff;
    --ink: #0a0a0a;
    --brand-blue: #0d7ad6;
    --band-text: #ffffff;
  }
  * { box-sizing: border-box; margin: 0; padding: 0; }
  html, body { width: 1200px; height: 694px; overflow: hidden; }
  body {
    background: var(--backdrop);
    font-family: "Lato", Arial, sans-serif;
    display: flex;
    align-items: center;
    justify-content: center;
    gap: 40px;
  }
  .card {
    position: relative;
    width: 540px;
    height: 316px;
    background: var(--card-white);
    border-radius: 26px;
    overflow: hidden;
    box-shadow: 0 14px 30px rgba(0,0,0,0.45);
  }
  .lockup {
    position: absolute;
    display: flex;
    flex-direction: column;
    align-items: flex-start;
  }
  .brand-name {
    display: flex;
    align-items: center;
    gap: 10px;
    font-family: "Lato", Arial, sans-serif;
    font-weight: 900;
    color: var(--ink);
    text-transform: uppercase;
    line-height: 1.05;
  }
  .brand-mark {
    background: var(--brand-blue);
    flex: none;
  }
  .brand-rule {
    height: 4px;
    background: var(--brand-blue);
  }
  .hotline {
    font-family: "Russo One", "Arial Black", sans-serif;
    color: var(--ink);
    line-height: 1;
  }

  /* front */
  .card--front .lockup { left: 38px; top: 78px; }
  .card--front .brand-name { font-size: 34px; }
  .card--front .brand-mark { width: 30px; height: 30px; }
  .card--front .brand-rule { width: 460px; margin: 12px 0 14px; }
  .card--front .hotline { font-size: 66px; letter-spacing: 2px; }

  /* back */
  .card--back .lockup { left: 34px; top: 30px; }
  .card--back .brand-name { font-size: 26px; }
  .card--back .brand-mark { width: 24px; height: 24px; }
  .card--back .brand-rule { width: 380px; margin: 8px 0 10px; }
  .card--back .hotline { font-size: 50px; letter-spacing: 2px; }

  .info-band {
    position: absolute;
    left: 0; right: 0; bottom: 0;
    height: 150px;
    background: var(--brand-blue);
    color: var(--band-text);
  }
  .services {
    position: absolute;
    right: 24px;
    top: 18px;
    list-style: none;
    font-size: 15px;
    line-height: 1.45;
    text-align: right;
  }
  .services li::before { content: "\2022\00a0"; }
  .contact {
    position: absolute;
    left: 30px;
    bottom: 20px;
  }
  .contact-name {
    font-size: 24px;
    font-weight: 700;
    margin-bottom: 6px;
  }
  .contact-line {
    display: flex;
    align-items: center;
    gap: 8px;
    font-size: 15px;
    line-height: 1.5;
  }
  .contact-line svg { width: 15px; height: 15px; fill: var(--band-text); flex: none; }
</style>
</head>
<body>

  <section class="card card--front" aria-label="Card front">
    <div class="lockup">
      <div class="brand-name"><span class="brand-mark"></span>Brindale Transport Maintenance</div>
      <div class="brand-rule"></div>
      <div class="hotline">0452819036</div>
    </div>
  </section>

  <section class="card card--back" aria-label="Card back">
    <div class="lockup">
      <div class="brand-name"><span class="brand-mark"></span>Brindale Transport Maintenance</div>
      <div class="brand-rule"></div>
      <div class="hotline">0452819036</div>
    </div>

    <div class="info-band">
      <ul class="services">
        <li>Brindale Transport Maintenance</li>
        <li>Onsite Cars &nbsp;&#8226;&nbsp;Trucks &amp; trailer</li>
        <li style="list-style:none">maintenance and repairs</li>
      </ul>

      <div class="contact">
        <div class="contact-name">Ronan Brindale</div>
        <div class="contact-line">
          <svg viewBox="0 0 24 24" aria-hidden="true"><path d="M6.6 10.8a15.1 15.1 0 0 0 6.6 6.6l2.2-2.2a1 1 0 0 1 1-.25 11.4 11.4 0 0 0 3.6.57 1 1 0 0 1 1 1V20a1 1 0 0 1-1 1A17 17 0 0 1 3 4a1 1 0 0 1 1-1h3.5a1 1 0 0 1 1 1c0 1.25.2 2.46.57 3.6a1 1 0 0 1-.25 1z"/></svg>
          <span>0452819036</span>
        </div>
        <div class="contact-line">
          <svg viewBox="0 0 24 24" aria-hidden="true"><path d="M2 5h20v14H2z M2 5l10 8 10-8" fill="none" stroke="#fff" stroke-width="2"/></svg>
          <span>Brindaletm@fernmail.com</span>
        </div>
      </div>
    </div>
  </section>

</body>
</html>
```